Retail Fitness Store requires Flyer for Women's Mini Marathon

Our retail store will be present as a vendor at a collection point for a women's mini marathon, target audience is 18-40
http://www.larkfieldladiesrun.ie

We need you to design a elegant flyer to be handed out on the day to advertise our fitness store focusing on female products. the following information needs to be shown, business name, address, contact number.

What we do, you can use images or text for the following, mini bands, power bands, rollers, knee sleeves, aerobic bars, vinyl dumbbells, hula hoops, women gloves, weightlifting belts, compression bv sports bras, compression tops / bottoms, ab rollers, pilates, yoga, fitness books.

Also mention we do a large range of other fitness equipment for strength training, olympic lifting, power lifting.

All information can be taking from our website www.quorvafit.com

Target Market(s)

18 - 40 female fitness enthusiats

Industry/Entity Type

Health And Wellness

Font styles to use
Sans Serif

Requirements
Must have
• Quorva Fitness Strore
• 5 & 6 Willowmere Yard
• Tansley Road Dublin
• 00353 1 628 9142
• www.quorvafit.com
Nice to have
• nice colour - a few images -
Should not have
• dark colours - image son men training or heavy weights
• please feel free to change the back ground colour of the logo that has been uploaded.

```html
<!DOCTYPE html>
<html lang="en">
<head>
<meta charset="utf-8">
<title>Quorva Fitness Strore – Flyer</title>
<link href="https://fonts.googleapis.com/css2?family=Exo+2:ital,wght@1,300;1,400;1,700;1,800;1,900&display=swap" rel="stylesheet">
<style>
  :root {
    --ink: #0b0b0c;
    --blue: #12a9dc;
    --blue-deep: #0b8fc2;
    --white: #ffffff;
    --grey-band: #5a5b5e;
    --stage: #a3a3a3;
    --list-ink: #111114;
  }
  * { margin: 0; padding: 0; box-sizing: border-box; }
  html, body { width: 1200px; height: 858px; overflow: hidden; }
  body {
    background: var(--stage);
    font-family: "Exo 2", sans-serif;
    position: relative;
  }
  .flyer {
    position: absolute;
    left: 308px; top: 19px;
    width: 584px; height: 820px;
    background: var(--ink);
    overflow: hidden;
    box-shadow: 0 10px 30px rgba(0,0,0,.35);
  }
  .flyer-shapes { position: absolute; inset: 0; width: 584px; height: 820px; }
  .hero-photo {
    position: absolute; left: 0; top: 0; width: 584px; height: 330px;
    background: radial-gradient(ellipse at 55% 60%, #4a4a4c 0%, #222224 45%, #0b0b0c 80%);
  }
  .headline {
    position: absolute; left: 0; top: 78px; width: 584px;
    text-align: center; color: var(--white);
    font-size: 33px; line-height: 44px; font-style: italic; font-weight: 300;
    text-transform: uppercase; letter-spacing: .2px;
  }
  .headline strong { color: var(--blue); font-weight: 800; }
  .product-shot {
    position: absolute; left: 261px; top: 306px; width: 284px; height: 138px;
    background: linear-gradient(135deg, #2a2a30 0%, #d85a9a 35%, #f0b43a 55%, #3a3a40 75%, #2f5fd0 100%);
    opacity: .55; border-radius: 6px;
  }
  .services { position: absolute; left: 96px; top: 436px; }
  .services-title {
    color: var(--blue); font-size: 20px; font-weight: 800; font-style: italic;
    text-transform: uppercase; margin-bottom: 6px;
  }
  .services-cols { display: flex; gap: 14px; }
  .services-list { list-style: none; }
  .services-list li {
    font-size: 13.4px; line-height: 18.4px; font-weight: 800; font-style: italic;
    text-transform: uppercase; color: var(--list-ink); white-space: nowrap;
  }
  .services-list li::before { content: "•"; color: var(--blue); margin-right: 5px; }
  .services-list.second { margin-left: 0; }
  .tagline {
    position: absolute; left: 101px; top: 627px;
    color: var(--blue); font-size: 14px; line-height: 18px; font-style: italic;
  }
  .tagline strong { color: var(--blue-deep); font-weight: 800; display: block; }
  .contact {
    position: absolute; right: 28px; top: 728px; text-align: right;
    color: var(--white); font-size: 13.5px; line-height: 17px; font-style: italic; font-weight: 300;
  }
  .brand {
    position: absolute; left: 30px; top: 742px; width: 130px;
    color: var(--blue); font-size: 18px; line-height: 20px; font-weight: 800; font-style: italic;
    text-transform: uppercase;
  }
  .web {
    position: absolute; left: 174px; top: 768px;
    color: var(--white); font-size: 23px; font-weight: 900; font-style: italic;
  }
</style>
</head>
<body>
  <article class="flyer">
    <div class="hero-photo" role="img" aria-label="Dark close-up photo of a kettlebell"></div>
    <svg class="flyer-shapes" viewBox="0 0 584 820" aria-hidden="true">
      <path d="M0,312 C150,240 400,300 584,268 L584,820 L0,820 Z" fill="var(--blue)"/>
      <path d="M0,410 C90,360 210,322 330,325 C440,328 520,348 584,342 L584,820 L0,820 Z" fill="var(--white)"/>
      <path d="M0,588 C60,700 260,735 584,648 L584,820 L0,820 Z" fill="var(--blue)"/>
      <path d="M0,610 C80,700 300,740 584,670 L584,820 L0,820 Z" fill="var(--white)"/>
      <path d="M0,648 C120,735 330,740 584,660 L584,820 L0,820 Z" fill="var(--ink)"/>
      <path d="M190,705 C360,700 480,680 584,650 L584,700 C470,712 330,712 190,705 Z" fill="var(--grey-band)"/>
      <path d="M170,715 C340,712 470,702 584,700 L584,765 C430,770 300,740 170,715 Z" fill="var(--blue)"/>
    </svg>

    <h1 class="headline">
      We are the <strong>premier shopping</strong><br>
      <strong>destination</strong> for all your<br>
      <strong>fitness equipment, clothing</strong><br>
      and <strong>accessory</strong> needs.
    </h1>

    <div class="product-shot" role="img" aria-label="Product cut-outs: compression top, knee sleeve, mini bands, kettlebell, sports bra and dumbbell set"></div>

    <section class="services">
      <h2 class="services-title">What we do</h2>
      <div class="services-cols">
        <ul class="services-list">
          <li>Mini bands</li>
          <li>Power bands</li>
          <li>Rollers</li>
          <li>Knee sleeves</li>
          <li>Aerobic bars</li>
          <li>Vinyl dumbbells</li>
          <li>Hula hoops</li>
          <li>Women gloves</li>
        </ul>
        <ul class="services-list second">
          <li>Weightlifting belts</li>
          <li>Compression BV sports bras</li>
          <li>Compression tops / bottoms</li>
          <li>Ab rollers</li>
          <li>Pilates</li>
          <li>Yoga</li>
          <li>Fitness books</li>
        </ul>
      </div>
    </section>

    <p class="tagline">we do a large range of other fitness equipment for
      <strong>strength training, olympic lifting, power lifting.</strong></p>

    <address class="contact">5 &amp; 6 Willowmere Yard, Tansley Road Dublin<br>00353 1 628 9142</address>

    <div class="brand">Quorva Fitness Strore</div>
    <div class="web">www.quorvafit.com</div>
  </article>
</body>
</html>
```